Need a fresh corporate identity for an existing Home Shopping Business in Thailand

We are one of the most active TV home shopping companies in Thailand. We need a fresh looking CI for our corporate, the colours of our corporate are Orange and Grey. We want our customers to see us as professional customer service who help them with their purchases.
The logo can be shown as a whole logo or either half logo but not less than half the logo.
Industry/Entity Type
Shopping
Requirements
Must have
- The logo should be shown at least half the logo or full logo.
Should not have
- The logo should not be shown less than half the logo.

```html
<!DOCTYPE html>
<html lang="en">
<head>
<meta charset="utf-8">
<title>Kindred Goods – Business Card</title>
<link rel="stylesheet" href="https://fonts.googleapis.com/css2?family=Source+Sans+3:wght@400;600&display=swap">
<style>
  :root {
    --backdrop: #e4e0dc;
    --card-white: #f4f4f2;
    --brand-orange: #e0662e;
    --brand-blue: #2f3c94;
    --ink: #2b2b2b;
    --faint-grey: #dcdcdc;
    --white: #ffffff;
  }
  * { margin: 0; padding: 0; box-sizing: border-box; }
  html, body {
    width: 1200px;
    height: 1000px;
    overflow: hidden;
    background: var(--backdrop);
    font-family: "Source Sans 3", "PT Sans", sans-serif;
  }
  .canvas {
    position: relative;
    width: 1200px;
    height: 1000px;
  }
  .card {
    position: absolute;
    top: 369px;
    width: 351px;
    height: 225px;
    overflow: hidden;
  }
  .card--front { left: 161px; background: var(--card-white); }
  .card--back  { left: 673px; background: var(--brand-blue); }

  /* large brand circle used as edge decoration */
  .edge-circle {
    position: absolute;
    border-radius: 50%;
  }
  .card--front .edge-circle {
    width: 220px; height: 220px;
    left: 240px; top: 2px;
    background: var(--faint-grey);
    opacity: 0.7;
  }
  .card--back .edge-circle {
    width: 230px; height: 230px;
    left: -118px; top: -2px;
    background: var(--brand-orange);
  }

  /* brand lockup */
  .brand {
    position: absolute;
    display: flex;
    flex-direction: column;
    align-items: center;
  }
  .brand__dot {
    border-radius: 50%;
  }
  .brand__name {
    font-weight: 600;
    white-space: nowrap;
  }
  .card--front .brand { left: 106px; top: 66px; width: 80px; }
  .card--front .brand__dot { width: 40px; height: 40px; background: var(--brand-orange); }
  .card--front .brand__name { margin-top: 7px; font-size: 9px; color: var(--brand-orange); }

  .card--back .brand { left: 172px; top: 82px; width: 120px; }
  .card--back .brand__dot { width: 46px; height: 46px; background: var(--white); }
  .card--back .brand__name { margin-top: 11px; font-size: 11.5px; color: var(--white); }

  /* contact details */
  .contact {
    position: absolute;
    right: 178px;
    top: 131px;
    list-style: none;
    text-align: right;
    font-size: 9.5px;
    line-height: 12.4px;
    color: var(--ink);
  }
  .contact__label { color: var(--brand-orange); }

  .person {
    position: absolute;
    left: 198px;
    top: 132px;
  }
  .person__name {
    font-size: 16px;
    font-weight: 400;
    color: var(--brand-orange);
    line-height: 18px;
  }
  .person__role {
    font-size: 13.5px;
    color: var(--ink);
    line-height: 16px;
  }
</style>
</head>
<body>
<main class="canvas">
  <section class="card card--front" aria-label="Business card front">
    <div class="edge-circle"></div>
    <div class="brand">
      <span class="brand__dot"></span>
      <span class="brand__name">Kindred Goods</span>
    </div>
    <ul class="contact">
      <li><span class="contact__label">A:</span> Lakeview Rd., Riverside,</li>
      <li>Harbor City 20500.</li>
      <li><span class="contact__label">T | F:</span> 02-555-0142 | 02-555-0143</li>
      <li><span class="contact__label">E:</span> hello@kindredgoods.biz</li>
      <li><span class="contact__label">W:</span> www.kindredgoodsshop.com</li>
    </ul>
    <div class="person">
      <p class="person__name">Niran Sato</p>
      <p class="person__role">Managing Partner</p>
    </div>
  </section>

  <section class="card card--back" aria-label="Business card back">
    <div class="edge-circle"></div>
    <div class="brand">
      <span class="brand__dot"></span>
      <span class="brand__name">Kindred Goods</span>
    </div>
  </section>
</main>
</body>
</html>
```